Brivolt VoIP COMMERCIAL PHONE FLYER

We are a full service telecom VoIP company that offers local, long distance calling plans to business clients. We offer local installations, and local service we have a hands on approach and will match or beat any competitor. We work with all types of business. We are fully HIPPA complient in the medical field

Target Market(s)

SMALL TO MEDIUM BUSINESS, Medical, Real Estate, Lawyer, Accounting

Industry/Entity Type

VoIP

Font styles to use
Serif

Colors
0054AA
0677BA
7BADD7
CADEEF
E8F1F8

Requirements
Must have
• Modern/ Current picture of phone reader friendly
Nice to have
• free flow, friendly, modern
Should not have
• stuffy, corporate feel

```html
<!DOCTYPE html>
<html lang="en">
<head>
<meta charset="utf-8">
<title>Brivolt VoIP Flyer</title>
<link href="https://fonts.googleapis.com/css2?family=Lato:wght@400;700;900&display=swap" rel="stylesheet">
<style>
  :root {
    --stage: #7a7a7a;
    --navy: #161d2b;
    --blue: #0677ba;
    --blue-panel: rgba(6, 106, 170, 0.86);
    --sky: #7badd7;
    --mist: #cadeef;
    --ice: #e8f1f8;
    --grey-band: #8c8e92;
    --white: #ffffff;
  }
  * { box-sizing: border-box; margin: 0; padding: 0; }
  html, body { width: 1200px; height: 1200px; overflow: hidden; }
  body {
    background: var(--stage);
    font-family: "Lato", sans-serif;
    position: relative;
  }
  .flyer {
    position: absolute;
    left: 152px; top: 20px;
    width: 896px; height: 1160px;
    background: var(--white);
    overflow: hidden;
  }
  .hero-photo {
    position: absolute; left: 0; top: 0;
    width: 100%; height: 660px;
    background: linear-gradient(135deg, var(--ice) 0%, #a9c3da 35%, #3c4a5e 60%, #d8b48a 85%, #f3ede4 100%);
  }
  .brand {
    position: absolute; left: 600px; top: 66px;
    width: 150px; height: 46px;
    background: var(--navy);
    display: flex; align-items: center; justify-content: center;
    color: var(--sky);
    font-weight: 900; font-size: 24px; letter-spacing: 1px;
  }
  .intro-band {
    position: absolute; left: 0; top: 650px;
    width: 100%; height: 220px;
    background: var(--navy);
  }
  .intro-text {
    position: absolute; left: 70px; top: 690px; width: 470px;
    color: var(--white); font-size: 27px; line-height: 1.22;
  }
  .intro-text strong { font-weight: 900; }
  .features {
    position: absolute; left: 560px; top: 480px;
    width: 336px; height: 330px;
    background: var(--blue-panel);
    padding: 30px 30px 0 40px;
    color: var(--white);
  }
  .feature {
    font-weight: 700; font-size: 22px; line-height: 1.2;
    text-transform: uppercase;
    padding: 22px 0;
    border-bottom: 1px solid var(--mist);
  }
  .feature:last-child { border-bottom: none; }
  .approach {
    position: absolute; left: 70px; top: 900px; width: 480px;
    color: var(--navy); font-size: 28px; line-height: 1.25;
  }
  .call-band {
    position: absolute; left: 0; top: 1024px;
    width: 100%; height: 48px;
    background: var(--grey-band);
    display: flex; align-items: center;
    padding-left: 80px; gap: 12px;
    color: var(--white); font-weight: 700; font-size: 26px;
  }
  .call-band svg { width: 30px; height: 30px; }
  .accent-line {
    position: absolute; left: 0; top: 1088px;
    width: 100%; height: 6px; background: var(--blue);
  }
  .footer {
    position: absolute; left: 0; top: 1094px;
    width: 100%; height: 66px;
    background: var(--navy);
    display: flex; align-items: center; justify-content: center; gap: 18px;
    color: var(--white); font-size: 20px; letter-spacing: 1px;
  }
  .device-photo {
    position: absolute; left: 590px; top: 830px;
    width: 290px; height: 230px;
    border-radius: 10px;
    background: linear-gradient(160deg, #2a2d33 0%, #4a6fa8 40%, #9fbfe0 60%, #1c1f24 100%);
  }
</style>
</head>
<body>
  <main class="flyer">
    <div class="hero-photo" role="img" aria-label="Photo of a hand dialling a modern office desk phone"></div>
    <div class="brand">Brivolt</div>

    <div class="intro-band"></div>
    <p class="intro-text">We are a full service telecom VoIP company that offers <strong>LOCAL, LONG DISTANCE CALLING PLANS TO BUSINESS CLIENTS.</strong></p>

    <section class="features">
      <div class="feature">Local Service</div>
      <div class="feature">Local Installations</div>
      <div class="feature">Fully HIPPA Complient in the Medical Field</div>
    </section>

    <p class="approach">We have a hands on approach and will match or beat any competitor.</p>

    <div class="call-band">
      <span>CALL US @</span>
      <svg viewBox="0 0 30 30" aria-hidden="true">
        <circle cx="15" cy="15" r="13" fill="none" stroke="#fff" stroke-width="2"/>
        <path d="M10.5 8.5l3 3-1.6 1.8c.9 1.8 2.1 3 3.9 3.9l1.8-1.6 3 3-1.8 1.9c-4.9-.5-9.7-5.3-10.2-10.2z" fill="#fff"/>
      </svg>
      <span>555 014 2278</span>
    </div>

    <div class="device-photo" role="img" aria-label="Photo of a touchscreen video desk phone with handset"></div>

    <div class="accent-line"></div>
    <footer class="footer">
      <span>info@brivolt.com</span><span>|</span><span>www.brivolt.com</span>
    </footer>
  </main>
</body>
</html>
```